Corvane Supplies Business Card

Professional business card that stand out to our potential customers. Front and back with clean modern design

Industry/Entity Type

Oil and gas

Contact Information for Business Card

Name, address, website , office phone and cell number

Requirements
Must have
• Editable files for each employee

```html
<!DOCTYPE html>
<html lang="en">
<head>
<meta charset="UTF-8">
<title>Corvane Supplies Business Card</title>
<link href="https://fonts.googleapis.com/css2?family=Montserrat:wght@400;700;800&family=Open+Sans:wght@400&display=swap" rel="stylesheet">
<style>
  :root {
    --teal: #05afd0;
    --red: #ff0000;
    --ink: #111111;
    --paper: #ffffff;
    --backdrop: #eeeced;
  }
  * { margin: 0; padding: 0; box-sizing: border-box; }
  html, body {
    width: 1200px; height: 1200px; overflow: hidden;
    background: var(--backdrop);
    font-family: "Montserrat", Arial, sans-serif;
    color: var(--ink);
  }
  .card {
    position: absolute;
    left: 222px;
    width: 721px; height: 433px;
    background: var(--paper);
    overflow: hidden;
  }
  .card--front { top: 147px; }
  .card--back { top: 631px; }
  .card__bands { position: absolute; inset: 0; width: 100%; height: 100%; }
  .band--teal { fill: var(--teal); }
  .band--red { fill: var(--red); }

  /* front */
  .front-brand {
    position: absolute; left: 0; right: 0; top: 150px;
    display: flex; align-items: center; justify-content: center; gap: 16px;
  }
  .brand-square { width: 58px; height: 58px; background: var(--teal); }
  .front-brand__name {
    font-weight: 800; color: var(--red);
    font-size: 40px; line-height: 1; letter-spacing: 0.5px;
  }
  .front-tagline {
    position: absolute; left: 0; right: 0; top: 298px;
    text-align: center;
    font-family: "Open Sans", Arial, sans-serif;
    font-size: 17px; letter-spacing: 7.4px;
  }

  /* back */
  .back-brand {
    position: absolute; left: 40px; width: 266px; top: 130px;
    display: flex; flex-direction: column; align-items: center; gap: 26px;
  }
  .back-brand .brand-square { width: 90px; height: 90px; }
  .back-brand__name {
    font-weight: 800; color: var(--red);
    font-size: 22px; letter-spacing: 0.5px; white-space: nowrap;
  }
  .person {
    position: absolute; right: 35px; top: 68px; text-align: right;
  }
  .person__name {
    font-weight: 700; color: var(--red);
    font-size: 31px; line-height: 1; letter-spacing: 0.5px;
  }
  .person__role { font-size: 21px; line-height: 1.2; margin-top: 2px; }
  .contacts {
    position: absolute; right: 30px; top: 160px;
    list-style: none; text-align: right;
  }
  .contacts li {
    display: flex; align-items: center; justify-content: flex-end;
    font-size: 21px; line-height: 26px; height: 26px; gap: 10px;
  }
  .contacts li + li { margin-top: 2px; }
  .contacts li:nth-child(2) { margin-top: 3px; }
  .contact-icon { width: 18px; height: 18px; flex: none; }
  .contact-icon circle.bg { fill: var(--teal); }
  .contact-icon .fg { fill: var(--paper); stroke: none; }
  .contact-icon .line { fill: none; stroke: var(--paper); stroke-width: 1.2; }
  .contacts .no-icon { padding-right: 28px; }
</style>
</head>
<body>

<section class="card card--front">
  <svg class="card__bands" viewBox="0 0 721 433" aria-hidden="true">
    <polygon class="band--teal" points="0,0 360,0 0,48"/>
    <polygon class="band--red" points="360,433 721,433 721,385"/>
  </svg>
  <div class="front-brand">
    <span class="brand-square"></span>
    <span class="front-brand__name">CORVANE<br>SUPPLIES</span>
  </div>
  <p class="front-tagline">your web / email address here</p>
</section>

<section class="card card--back">
  <svg class="card__bands" viewBox="0 0 721 433" aria-hidden="true">
    <polygon class="band--teal" points="0,0 360,0 0,48"/>
    <polygon class="band--red" points="360,433 721,433 721,385"/>
  </svg>
  <div class="back-brand">
    <span class="brand-square"></span>
    <span class="back-brand__name">CORVANE SUPPLIES</span>
  </div>
  <div class="person">
    <h1 class="person__name">NAME HERE</h1>
    <p class="person__role">Graphic Designer</p>
  </div>
  <ul class="contacts">
    <li>+000 00 00 00 00
      <svg class="contact-icon" viewBox="0 0 18 18"><circle class="bg" cx="9" cy="9" r="9"/><circle class="fg" cx="9" cy="6.5" r="2.4"/><path class="fg" d="M4.8 13.2a4.2 3.6 0 0 1 8.4 0z"/></svg>
    </li>
    <li>+000 00 00 00 00
      <svg class="contact-icon" viewBox="0 0 18 18"><circle class="bg" cx="9" cy="9" r="9"/><path class="fg" d="M6.3 4.8l1.6-.4.8 2.1-1 .8c.4 1 1.1 1.8 2 2.3l.9-.9 2 .9-.4 1.6c-3.4.3-6.1-2.8-5.9-6.4z"/></svg>
    </li>
    <li>www.your website here
      <svg class="contact-icon" viewBox="0 0 18 18"><circle class="bg" cx="9" cy="9" r="9"/><circle class="line" cx="9" cy="9" r="4.6"/><ellipse class="line" cx="9" cy="9" rx="2" ry="4.6"/><path class="line" d="M4.4 9h9.2"/></svg>
    </li>
    <li>23 anywhere st, any city
      <svg class="contact-icon" viewBox="0 0 18 18"><circle class="bg" cx="9" cy="9" r="9"/><path class="fg" d="M9 14s-3.6-3.8-3.6-6.3a3.6 3.6 0 0 1 7.2 0C12.6 10.2 9 14 9 14z"/><circle cx="9" cy="7.6" r="1.3" fill="#05afd0"/></svg>
    </li>
    <li class="no-icon">Po.Box - 00</li>
  </ul>
</section>

</body>
</html>
```